Post card

I want an educational customer postcard with our logo, email, and contact number. We are a residential foundation inspection & repair company here in Los Angeles. We provide foundation repair, earthquake retrofitting, and reinforcement.
Our number is 323-555-0148.
Email info@brenvoltdesk.com
Our license number is #3862917

OUR GOAL
Our primary objective is to empower clients with comprehensive knowledge about foundation issues and earthquake retrofitting. By educating them on the potential risks associated with foundation problems and the importance of earthquake retrofitting, we aim to equip homeowners with the necessary information to make informed decisions about safeguarding their properties. Highlighting the benefits of having their houses properly bolted not only enhances structural integrity but also provides peace of mind during seismic events, ensuring the safety and security of their homes and loved ones.

```html
<!DOCTYPE html>
<html lang="en">
<head>
<meta charset="utf-8">
<title>Brenvolt Desk Postcard</title>
<link rel="stylesheet" href="https://fonts.googleapis.com/css2?family=Saira:wght@400;500;600;700&display=swap">
<style>
  :root{
    --stage:#4a4a4a;
    --paper:#ffffff;
    --ink:#151515;
    --brand-blue:#3d66b5;
    --brand-blue-soft:#c9d5ee;
    --brand-red:#d6232a;
    --panel-dark:#2e2e2e;
    --rule:#9a9a9a;
  }
  html,body{margin:0;padding:0;}
  body{
    width:1200px;height:436px;overflow:hidden;
    background:var(--stage);
    font-family:"Saira",sans-serif;
    position:relative;
  }
  .postcard{
    position:absolute;top:32px;width:557px;height:371px;
    background:var(--paper);
    box-shadow:0 4px 10px rgba(0,0,0,.45);
    overflow:hidden;
  }
  .postcard--front{left:32px;}
  .postcard--back{left:611px;}
  .postcard svg{display:block;width:100%;height:100%;}
  .brand-name{font-weight:700;fill:var(--brand-blue);letter-spacing:1px;}
  .contact{font-weight:600;fill:var(--ink);font-size:30px;}
  .headline{font-weight:600;font-size:62px;fill:var(--ink);}
  .headline .accent{fill:var(--brand-red);}
  .services{font-weight:500;font-size:29px;fill:#fff;}
  .license{font-weight:500;font-size:19px;fill:#fff;}
  .goal-title{font-weight:700;font-size:54px;fill:var(--brand-red);}
  .goal-copy{font-weight:500;font-size:23.5px;fill:#fff;}
</style>
</head>
<body>

<section class="postcard postcard--front" aria-label="Postcard front">
  <svg viewBox="0 0 1196 797" preserveAspectRatio="none">
    <defs>
      <linearGradient id="front-wash" x1="0" y1="0" x2="0" y2="1">
        <stop offset="0" stop-color="#ffffff"/>
        <stop offset="0.55" stop-color="#eef2fa"/>
        <stop offset="0.8" stop-color="#7f9bd2"/>
        <stop offset="1" stop-color="#3d66b5"/>
      </linearGradient>
      <linearGradient id="photo-tones" x1="0" y1="0" x2="1" y2="1">
        <stop offset="0" stop-color="#d9dde2"/>
        <stop offset="0.5" stop-color="#a9b3c2"/>
        <stop offset="1" stop-color="#b8755a"/>
      </linearGradient>
    </defs>
    <rect class="front-background" width="1196" height="797" fill="url(#front-wash)"/>
    <path class="photo-area" role="img" aria-label="Photo of two builders in hard hats reading a blueprint at a construction site"
      d="M700,640 L850,280 Q880,190 960,210 L1196,300 L1196,797 L430,797 Q640,720 700,640 Z" fill="url(#photo-tones)"/>
    <path class="blue-swoosh" d="M690,665 L815,265 Q855,150 965,178 L1196,268 L1196,300 L960,210 Q880,190 850,280 L705,650 Z" fill="var(--brand-blue)"/>
    <path class="red-swoosh" d="M430,797 L700,640 L520,797 Z" fill="var(--brand-red)"/>

    <rect class="brand-mark" x="41" y="50" width="80" height="80" fill="var(--brand-blue)"/>
    <text class="brand-name" x="142" y="88" font-size="50">BRENVOLT</text>
    <text class="brand-name" x="142" y="142" font-size="50">DESK</text>

    <g class="contact-phone" fill="var(--brand-red)">
      <path d="M785,52 q-4,4 0,14 q6,12 16,16 q8,3 11,-1 l-5,-6 q-3,2 -6,0 q-5,-4 -8,-10 q-1,-3 2,-5 Z"/>
    </g>
    <text class="contact" x="826" y="72">323-555-0148</text>
    <g class="contact-mail" fill="none" stroke="var(--brand-red)" stroke-width="3">
      <rect x="781" y="92" width="30" height="20"/>
      <path d="M781,92 L796,104 L811,92"/>
    </g>
    <text class="contact" x="826" y="112">info@brenvoltdesk.com</text>

    <text class="headline" x="41" y="291">We are a <tspan class="accent">Residential</tspan></text>
    <text class="headline accent" x="41" y="357" fill="var(--brand-red)">Foundation Inspection</text>
    <text class="headline" x="41" y="423">&amp; <tspan class="accent">Repair Company</tspan></text>
    <text class="headline" x="41" y="488">here in Los Angeles.</text>

    <line class="services-rule" x1="41" y1="579" x2="41" y2="716" stroke="var(--brand-red)" stroke-width="2"/>
    <text class="services" x="59" y="620">We provide foundation repair,</text>
    <text class="services" x="59" y="656">earthquake retrofitting,</text>
    <text class="services" x="59" y="692">and reinforcement.</text>

    <text class="license" x="41" y="773">Our license number is #3862917</text>
  </svg>
</section>

<section class="postcard postcard--back" aria-label="Postcard back">
  <svg viewBox="0 0 1196 797" preserveAspectRatio="none">
    <defs>
      <linearGradient id="ruin-tones" x1="0" y1="0" x2="0" y2="1">
        <stop offset="0" stop-color="#2e2e2e"/>
        <stop offset="0.5" stop-color="#4a423c"/>
        <stop offset="1" stop-color="#5c4d42"/>
      </linearGradient>
      <clipPath id="panel-shape">
        <path d="M0,0 L560,0 Q690,30 700,140 L650,420 Q640,470 600,500 Q570,540 585,600 L610,797 L0,797 Z"/>
      </clipPath>
    </defs>
    <rect width="1196" height="797" fill="var(--paper)"/>
    <path class="blue-swoosh" d="M360,0 L600,0 Q715,40 722,160 L672,420 L700,140 Q690,30 560,0 Z" fill="var(--brand-blue)"/>
    <path class="panel" d="M0,0 L560,0 Q690,30 700,140 L650,420 Q640,470 600,500 Q570,540 585,600 L610,797 L0,797 Z" fill="var(--panel-dark)"/>
    <rect class="photo-area" role="img" aria-label="Photo of a house damaged by an earthquake" clip-path="url(#panel-shape)"
      x="0" y="540" width="700" height="257" fill="url(#ruin-tones)"/>
    <path class="red-swoosh" d="M585,580 L665,797 L612,797 Z" fill="var(--brand-red)"/>

    <text class="goal-title" x="45" y="83">OUR GOAL</text>
    <g class="goal-copy">
      <text x="45" y="123">Our primary objective is to empower clients with</text>
      <text x="45" y="152">comprehensive knowledge about foundation</text>
      <text x="45" y="181">issues and earthquake retrofitting.</text>
      <text x="45" y="228">By educating them on the potential risks</text>
      <text x="45" y="257">associated with foundation problems and the</text>
      <text x="45" y="286">importance of earthquake retrofitting, we aim to</text>
      <text x="45" y="315">equip homeowners with the necessary</text>
      <text x="45" y="344">information to make informed decisions about</text>
      <text x="45" y="373">safeguarding their properties.</text>
      <text x="45" y="412">Highlighting the benefits of having their houses</text>
      <text x="45" y="441">properly bolted not only enhances structural</text>
      <text x="45" y="470">integrity but also provides peace of mind during</text>
      <text x="45" y="499">seismic events, ensuring the safety and security</text>
      <text x="45" y="528">of their homes and loved ones.</text>
    </g>

    <rect class="stamp-box" x="877" y="107" width="164" height="164" fill="none" stroke="var(--rule)" stroke-width="2"/>
    <g class="address-lines" stroke="var(--rule)" stroke-width="2">
      <line x1="755" y1="371" x2="1163" y2="371"/>
      <line x1="755" y1="425" x2="1163" y2="425"/>
      <line x1="755" y1="479" x2="1163" y2="479"/>
      <line x1="755" y1="533" x2="1163" y2="533"/>
      <line x1="755" y1="587" x2="1163" y2="587"/>
    </g>
  </svg>
</section>

</body>
</html>
```